helping new make my new business shine, with your design for : Corvaline Apparel

Create business card for Corvaline Apparel,( which means to shine in French)
I'm starting up a new online retail clothing store. My main voice is to sell outfit for Church and church events for men and women. (But geared more towards women)
1. photos included are from a catolog of the clothes that will be on my web site
2. Create your owns look keeping my example in mind.
3 . I want small articles of clothing on the card a few dresses, some pants, men suit
women hats, one in each corner of the card., sunglasses.all these articles are to be placed on the front of my business card to show my inventory. I want people to look at my business card and want to check out my web site.
Place each of these written out in different areas on the card clergy robes, usher uniforms, egyptian linen, men's accessories. sunglasses
4. Make your article of clothing BLING I like things that sparkle
5. On the back side will be all the contact information. The letters are to be in English or Script if you can make the business name lettering in 3D would be great but not nessassary.
Corvaline Apparel
Order online 24/7 at: corvalineapparel.example
Bus/Fax 555-314-7092
Mon-Wed 8:00am till 12:00 pm mst.
Ruth Pembley, Owner
ruthpembley45@mailbox.example

I'm looking forward to receiving some outstanding designs. I known the space your working with is small but when creating the women's attire and hats make them bling where possible more is better as long as it's elegant. Thank you Added Sunday, August 7, 2016

Target Market(s)

Christains women& men who take pride in what they wear to church, and who just want to look good at any high dollar event without having to spent a lot.

Industry/Entity Type

Fashion

Contact Information for Business Card

The words need to be jumping out at you (3D lettering,) but ONLY if they can be done elegantly,
Corvaline Apparel
Order online at: corvalineapparel.example
555-314-7093
Ruth Pembley, CEO
All the contact information to be placed on the backside

Font styles to use
Decorative
Script

Requirements
Must have
• Everything I stated in the project description.
• Bling on the women attire photos and hats
• -Ok to use the photos that are attached in your business card submission (please refrain from using the model's faces, only the clothing)
• -I do not have logo but please just use the business name is a creative way
Nice to have
• Everything's indicated
Should not have
• 1. The drawings should not use my photos but create a new look.
• 2. Do Not Use a black backing

```html
<!DOCTYPE html>
<html lang="en">
<head>
<meta charset="utf-8">
<title>Corvaline Apparel – Business Card</title>
<link rel="stylesheet" href="https://fonts.googleapis.com/css2?family=Great+Vibes&family=Lora:ital,wght@1,400&display=swap">
<style>
  :root {
    --page: #f2ebe3;
    --card: #cb6363;
    --card-edge: #e7c76c;
    --ink: #1b1010;
    --silhouette: #6a2d2f;
    --silver-light: #eceef2;
    --silver-mid: #b9bcc3;
    --silver-dark: #8d9099;
  }
  * { margin: 0; padding: 0; box-sizing: border-box; }
  html, body { width: 1073px; height: 1200px; overflow: hidden; background: var(--page); }
  .canvas { position: relative; width: 1073px; height: 1200px; }

  .card { position: absolute; background: var(--card); overflow: hidden; }
  .card--front { left: 86px; top: 51px; width: 866px; height: 489px; border: 1.5px solid var(--card-edge); }
  .card--back { left: 80px; top: 593px; width: 873px; height: 492px; }

  .sparkle-item {
    position: absolute;
    background: radial-gradient(circle at 35% 30%, var(--silver-light), var(--silver-mid) 55%, var(--silver-dark));
    border-radius: 8px;
  }

  .category {
    position: absolute;
    font-family: "Great Vibes", cursive;
    font-size: 31px;
    color: var(--ink);
    white-space: nowrap;
    transform-origin: left center;
  }
  .category--accessories { left: 14px; top: 32px; transform: rotate(-12deg); }
  .category--ushers { left: 645px; top: 34px; transform: rotate(-11deg); }
  .category--sunglasses { left: 718px; top: 262px; transform: rotate(-15deg); }
  .category--clergy { left: 14px; top: 330px; transform: rotate(40deg); }
  .category--linen { left: 418px; top: 412px; transform: rotate(5deg); }

  .brand-title {
    position: absolute; left: 150px; top: 138px; width: 620px;
    text-align: center;
    font-family: "Great Vibes", cursive;
    font-size: 78px; line-height: 1;
    color: var(--ink);
    text-shadow: 2px 2px 0 rgba(0,0,0,0.15);
  }
  .brand-rule { position: absolute; left: 163px; top: 253px; width: 588px; height: 4px; background: var(--ink); }

  .contact { position: absolute; left: 64px; top: 100px; color: var(--ink); }
  .contact__name { font-family: "Great Vibes", cursive; font-size: 50px; line-height: 1.1; }
  .contact__line { font-family: "Lora", serif; font-style: italic; font-size: 31px; line-height: 38px; white-space: nowrap; }

  .silhouette { position: absolute; top: 368px; height: 110px; background: var(--silhouette); border-radius: 6px; }
</style>
</head>
<body>
<main class="canvas">

  <section class="card card--front" aria-label="Business card front">
    <span class="category category--accessories">men's accesories</span>
    <span class="category category--ushers">usher uniforms</span>
    <span class="category category--sunglasses">sunglasses</span>
    <span class="category category--clergy">clergy robes</span>
    <span class="category category--linen">egyptian linen</span>

    <div class="sparkle-item" style="left:265px;top:19px;width:51px;height:117px" role="img" aria-label="Sparkling silver fitted dress"></div>
    <div class="sparkle-item" style="left:588px;top:26px;width:58px;height:31px" role="img" aria-label="Sparkling silver bow tie"></div>
    <div class="sparkle-item" style="left:16px;top:144px;width:32px;height:109px" role="img" aria-label="Sparkling silver necktie"></div>
    <div class="sparkle-item" style="left:744px;top:199px;width:111px;height:40px" role="img" aria-label="Sparkling silver sunglasses"></div>
    <div class="sparkle-item" style="left:245px;top:391px;width:54px;height:82px" role="img" aria-label="Sparkling silver vest"></div>
    <div class="sparkle-item" style="left:684px;top:345px;width:77px;height:133px" role="img" aria-label="Sparkling silver flared dress"></div>

    <h1 class="brand-title">Corvaline Apparel</h1>
    <div class="brand-rule"></div>
  </section>

  <section class="card card--back" aria-label="Business card back">
    <div class="contact">
      <p class="contact__name">Corvaline Apparel</p>
      <p class="contact__line">Order online 24/7 at: corvalineapparel.example</p>
      <p class="contact__line">Bus/Fax 555-314-7092</p>
      <p class="contact__line">Mon-Wed 8:00am till 12:00 pm mst.</p>
      <p class="contact__line">Ruth Pembley, Owner</p>
      <p class="contact__line">ruthpembley45@mailbox.example</p>
    </div>
    <div class="silhouette" style="left:78px;width:82px" role="img" aria-label="Men's suit jacket silhouette"></div>
    <div class="silhouette" style="left:182px;width:83px" role="img" aria-label="Blazer silhouette"></div>
    <div class="silhouette" style="left:304px;width:63px" role="img" aria-label="Short dress silhouette"></div>
    <div class="silhouette" style="left:395px;width:76px" role="img" aria-label="Long dress silhouette"></div>
  </section>

</main>
</body>
</html>
```